Buch-/eBook-Cover im Bereich Spiritueller Ratgeber / Persönlichkeitsentwicklung
Zielgruppe
siehe Briefing-pdf.
Aufgabenstellung
E-Book E-Book"
Das Design darf nicht zu überladen sein.

```html
<!DOCTYPE html>
<html lang="de">
<head>
<meta charset="utf-8">
<title>ICH HERZ WESEN – Buchumschlag</title>
<link rel="stylesheet" href="https://fonts.googleapis.com/css2?family=Literata:ital,wght@0,400;0,600;0,700;1,400;1,600&family=Playfair+Display:wght@900&family=Great+Vibes&family=Nunito+Sans:wght@400&display=swap">
<style>
:root{
  --paper:#ffffff;
  --trim:#8a8a8a;
  --back-top:#7a4650;
  --back-mid:#7a3e7e;
  --back-bottom:#4a2a8a;
  --spine-top:#5a3a3c;
  --spine-bottom:#4c2f86;
  --photo-top:#5d4033;
  --photo-mid:#6a4a3e;
  --photo-bottom:#4a2e7a;
  --gold:#d8b56c;
  --gold-soft:#c9ad74;
  --text-light:#f4eaf0;
  --lilac:#d9a9d6;
  --blush:#f6dde6;
}
*{margin:0;padding:0;box-sizing:border-box}
html,body{width:1200px;height:869px;overflow:hidden;background:var(--paper)}
.canvas{position:relative;width:1200px;height:869px;background:var(--paper)}
.trim-frame{position:absolute;left:51px;top:69px;width:1091px;height:734px;border:1px solid var(--trim)}
.spine-guide{position:absolute;top:69px;height:734px;border-left:1px solid var(--trim)}
.spine-guide.left{left:562px}
.spine-guide.right{left:632px}

.back-cover{position:absolute;left:68px;top:86px;width:494px;height:701px;
  background:linear-gradient(180deg,var(--back-top) 0%,var(--back-mid) 50%,var(--back-bottom) 100%);
  font-family:"Literata",serif;color:var(--text-light)}
.back-glow{position:absolute;inset:0;
  background:radial-gradient(circle at 85% 40%,rgba(230,110,170,.35),transparent 45%),
             radial-gradient(circle at 20% 85%,rgba(220,100,190,.3),transparent 40%)}
.back-portrait{position:absolute;left:302px;top:380px;width:170px;height:321px;
  background:linear-gradient(180deg,#6b4a4e 0%,#b0477f 45%,#5a2f9a 100%);border-radius:80px 80px 0 0;opacity:.85}
.blurb{position:absolute;left:71px;width:347px;font-size:9.2px;line-height:12.7px;text-align:justify}
.blurb.intro{top:69px;font-weight:600}
.blurb.about{top:123px}
.audience{position:absolute;left:71px;top:258px;font-size:11px;line-height:15.6px;font-weight:600;letter-spacing:-.2px;white-space:nowrap}
.quote{position:absolute;left:71px;top:355px;width:347px;font-size:12px;line-height:17px;font-style:italic;font-weight:600;color:var(--gold)}
.bio-heading{position:absolute;left:71px;top:430px;font-size:11px;font-weight:700}
.bio{position:absolute;left:71px;top:462px;width:222px;font-size:9.2px;line-height:12.7px;text-align:justify}
.bio em{font-size:10.5px}

.spine{position:absolute;left:562px;top:86px;width:70px;height:701px;
  background:linear-gradient(180deg,var(--spine-top),var(--spine-bottom))}
.spine-author{position:absolute;top:60px;width:100%;text-align:center;font-family:"Literata",serif;font-style:italic;font-size:16px;line-height:22px;color:var(--blush)}
.spine-title{position:absolute;left:35px;top:355px;transform:translate(-50%,-50%) rotate(-90deg);white-space:nowrap;
  font-family:"Literata",serif;font-weight:700;font-size:26px;letter-spacing:.5px;color:var(--lilac)}
.imprint{font-family:"Literata",serif;font-weight:400;text-align:center;color:var(--gold-soft)}
.spine .imprint{position:absolute;top:618px;width:100%;font-size:13px;line-height:16px;color:#d8cde6}
.front-cover .imprint{position:absolute;left:352px;top:610px;width:130px;font-size:19px;line-height:22px}

.front-cover{position:absolute;left:632px;top:86px;width:493px;height:701px;overflow:hidden}
.cover-photo{position:absolute;inset:0;
  background:linear-gradient(180deg,var(--photo-top) 0%,var(--photo-mid) 45%,var(--photo-bottom) 100%)}
.photo-figure{position:absolute;right:0;top:60px;width:300px;height:641px;border-radius:150px 150px 0 0;
  background:linear-gradient(180deg,#3a2624 0%,#b08a7a 25%,#c23f9a 55%,#5a2ea6 80%)}
.title{position:absolute;left:33px;top:58px;font-family:"Playfair Display",serif;font-weight:900;font-size:58px;line-height:62px;color:var(--gold)}
.subtitle{position:absolute;left:34px;top:248px;font-family:"Nunito Sans",sans-serif;font-size:13px;color:var(--text-light)}
.tagline{position:absolute;left:34px;top:308px;width:230px;font-family:"Literata",serif;font-size:15px;line-height:21px;color:#efe4e6}
.author-signature{position:absolute;left:33px;top:596px;font-family:"Great Vibes",cursive;font-size:40px;color:var(--blush)}
</style>
</head>
<body>
<div class="canvas">
  <div class="trim-frame"></div>

  <section class="back-cover">
    <div class="back-glow" role="img" aria-label="Lichtpunkte in Rosa und Violett als Hintergrund"></div>
    <div class="back-portrait" role="img" aria-label="Porträt der Autorin im violetten Blazer"></div>
    <p class="blurb intro">In der Lebensmitte ändert die Seele ihre Bedürnisse und stellt eine Frage, die sich nicht mehr ignorieren lässt: „Wer bin ich – jenseits aller Rollen, Masken und Erwartungen?“</p>
    <p class="blurb about"><strong>Mirela Anna Kessler</strong> – Mentorin, Expertin für schamanische Ahnenarbeit und Autorin des Bestsellers „Schamanische Ahnenwege“ – führt dich auf einem spiralförmigen Weg der Selbstwerdung durch drei transformative Ebenen: Von der psychologischen Dekonditionierung des „ICH“ über die seelische Heimkehr durch „Ahnenarbeit und weibliche Schöpferkraft“ bis zur „Verkörperung des SELBST im Alltag“ – in Authentizität, Würde und tiefer Seelenbehaglichkeit. Was dieses Buch von anderen unterscheidet: Es verbindet westliche Psychologie mit schamanischer Tradition, spirituelle Tiefe mit praktischer Anwendbarkeit – und gelebte Erfahrung mit fundierter Methodik.</p>
    <p class="audience">Für Frauen, die spüren, dass ihre alte Haut zu eng geworden ist.<br>Für Frauen, die bereit sind, ganz sie selbst zu werden.<br>Für Frauen, die nach Hause kommen wollen – zu sich selbst.</p>
    <p class="quote">„Denn tief in uns wissen wir: Wir sind die, auf die wir gewartet haben.“</p>
    <h3 class="bio-heading">Autorinnenzeile:</h3>
    <p class="bio"><em>Mirela Anna Kessler</em> ist Mentorin für ganzheitliche Selbstentwicklung, Expertin für schamanische Ahnenarbeit und Künstlerin. Seit über drei Jahrzehnten begleitet sie Menschen auf dem Weg zu ihrer wahren Essenz. Ihr Bestseller „Schamanische Ahnenwege“ (Lindtal Verlag, 2021) hat tausenden Menschen geholfen, ihre Wurzeln zu klären und das gute Erbe ihrer Vorfahren zu empfangen. Sie lebt und arbeitet im Klosterdorf Hallbach.</p>
  </section>

  <section class="spine">
    <p class="spine-author">Mirela<br>Anna<br>Kessler</p>
    <p class="spine-title">ICH • HERZ • WESEN</p>
    <p class="imprint">NOVA<br>Edition</p>
  </section>

  <section class="front-cover">
    <div class="cover-photo" role="img" aria-label="Foto der lächelnden Autorin im violetten Blazer vor einer alten Holztür">
      <div class="photo-figure"></div>
    </div>
    <h1 class="title">ICH<br>HERZ<br>WESEN</h1>
    <p class="subtitle">ERWACHEN IN DER LEBENMITTE</p>
    <p class="tagline">Die Initiation zu weiblicher Souveränität, verkörperter Wahrheit und tiefer Seelenbehaglichkeit</p>
    <p class="author-signature">Mirela Anna Kessler</p>
    <p class="imprint">NOVA Edition</p>
  </section>

  <div class="spine-guide left"></div>
  <div class="spine-guide right"></div>
</div>
</body>
</html>
```